Rapidly Expanding Real Estate Firm Seeking Signage Designs for Multiple Properties

We would like a sign design template created that we can use at our apartment buildings. We would like a consistent sign appearance that is adaptable enough to be used at different locations, on different mediums, and in different sizes. All vary for signage depending on the local laws and regulations as well as the type and style of the property. But the sign design should be consistent enough to support our company's branding efforts; so people that see our sign know its our company but also that the specific property is unique. Our thought was to incorporate the property address; i.e. "418 Larkwood" along with a portion of our company logo(attached). Then tag our website address across the bottom. Or some combination of that structure/design. It may make sense to just use the address and website address across the bottom OR it might be good to say 418 Larkwood St in large font with "by Amber Ridge Holdings Group" underneath as sort of a tag line. Not quite sure.
But we definitely want the signage to be clearly visible, professional, and clean. Easily read for the street. Should be flexible enough to work on metal or wood or any other medium with updates for the address and maybe color.
This is not a for sale sign design request. The sign concept will be used at apartment buildings. Sample property photos are attached - we are looking for a design template that is flexible enough to work on various property types. Also could be wall mounted or a pylon sign. Concept should work either way.

Target Market(s)

Prospective Tenants 25-45 yrs of age with incomes ranging from $55k - $95k.

Industry/Entity Type

Real Estate - Apartments

Colors
59FF00
82FF00
B8FF75
E3FFCB
F4FFEA

Requirements
Must have
• The street address number, web address(www.amberridgeholdingsgroup.example), & incorporate our primary colors(green,white,black)
Nice to have
• "418 Larkwood St." by Amber Ridge
Should not have
• Should not say For Sale, For Lease, post our phone number.

```html
<!DOCTYPE html>
<html lang="en">
<head>
<meta charset="utf-8">
<title>Amber Ridge Holdings Group – Property Sign</title>
<link rel="stylesheet" href="https://fonts.googleapis.com/css2?family=Anton&family=Roboto+Condensed:wght@700&display=swap">
<style>
  :root {
    --backdrop: #e9ecef;
    --sign-black: #0a090b;
    --brand-green: #7dc242;
    --sign-white: #ffffff;
    --ink: #121212;
  }
  * { margin: 0; padding: 0; box-sizing: border-box; }
  html, body {
    width: 1200px;
    height: 800px;
    overflow: hidden;
    background: var(--backdrop);
  }
  .canvas {
    width: 1200px;
    height: 800px;
    display: flex;
    align-items: center;
    justify-content: center;
  }
  .sign {
    width: 440px;
    height: 740px;
    display: flex;
    flex-direction: column;
    box-shadow: 0 10px 30px rgba(0,0,0,0.18);
    font-family: "Roboto Condensed", "Arial Narrow", sans-serif;
  }
  .sign__brand {
    height: 274px;
    background: var(--sign-black);
    display: flex;
    flex-direction: column;
    align-items: center;
    justify-content: center;
    padding-top: 60px;
  }
  .brand-name {
    display: flex;
    align-items: center;
    gap: 10px;
    color: var(--brand-green);
    font-weight: 700;
    text-transform: uppercase;
  }
  .brand-name__mark {
    width: 14px;
    height: 14px;
    background: var(--brand-green);
  }
  .brand-name__primary {
    font-size: 40px;
    letter-spacing: 1px;
    line-height: 1;
  }
  .brand-name__secondary {
    margin-top: 10px;
    color: var(--brand-green);
    font-weight: 700;
    font-size: 17px;
    letter-spacing: 3px;
    text-transform: uppercase;
  }
  .sign__stripe {
    height: 14px;
    background: var(--brand-green);
  }
  .sign__property {
    height: 214px;
    background: var(--sign-white);
    display: flex;
    flex-direction: column;
    align-items: center;
    justify-content: center;
    gap: 8px;
  }
  .property-address {
    color: var(--ink);
    font-size: 52px;
    line-height: 1;
    font-weight: 700;
  }
  .property-type {
    font-family: "Anton", "Impact", sans-serif;
    font-weight: 400;
    color: var(--brand-green);
    font-size: 80px;
    line-height: 1.05;
    letter-spacing: 1px;
  }
  .sign__contact {
    flex: 1;
    background: var(--brand-green);
    display: flex;
    flex-direction: column;
    align-items: center;
    justify-content: center;
    gap: 16px;
    color: var(--sign-white);
    font-weight: 700;
  }
  .contact-tagline {
    font-size: 28px;
    line-height: 1;
  }
  .contact-web {
    font-size: 23px;
    line-height: 1;
  }
</style>
</head>
<body>
  <main class="canvas">
    <article class="sign">
      <header class="sign__brand">
        <div class="brand-name">
          <span class="brand-name__mark"></span>
          <span class="brand-name__primary">Amber Ridge</span>
        </div>
        <div class="brand-name__secondary">Holdings Group LLC</div>
      </header>
      <div class="sign__stripe"></div>
      <section class="sign__property">
        <h1 class="property-address">418 Larkwood St.</h1>
        <p class="property-type">APARTMENTS</p>
      </section>
      <footer class="sign__contact">
        <p class="contact-tagline">by Amber Ridge Holdings Group</p>
        <p class="contact-web">www.amberridgeholdingsgroup.example</p>
      </footer>
    </article>
  </main>
</body>
</html>
```